Clinic Harbor brouchure

I am attaching a sample of what I would like to be created in a vector format or format that I can send to a printer.

The Clinic Harbor logo is the style I like.

Thanks, Alan
Updates

Project Deadline Extended Reason: I have extended the deadline. Thanks for your understanding.Sincerely, Alan Added Friday, March 24, 2017

Industry/Entity Type

Printer

Font styles to use
Other font styles liked:
• please see attached

Requirements
Must have
• please create a format that I can provide to a printer for making a brochure
• UPDATE: please if possible, have the size be 10'' wide by 11'' tall
• with the brochure opening from top to bottom like a calendar
Nice to have
• I like where you are going with this, can you put an image on the top of the page and the text on the bottom of the page
• when you are holding the marketing piece, it should be 10'' wide by 5.5'' tall, after you open the cover page, then it becomes 10'' wide by 11'' tall
• the top page is an image and the lower page is the message..
• so when you view it you see a picture and then text
• the front cover should have the logo image -
• Clinic Harbor
• the wording - cost effective resources for your practice
• cash back medical plans, 15% medical wellness discount
• on the inside pages 1-3 keep the tag line Clinic Harbor / Practice Management
• the contact info on page 4
• the last page - Clinic Harbor logo in the middle, then Practice Management on the bottom

```html
<!DOCTYPE html>
<html lang="en">
<head>
<meta charset="utf-8">
<title>Clinic Harbor – Brochure Spread</title>
<link href="https://fonts.googleapis.com/css2?family=Roboto+Condensed:wght@400;700&display=swap" rel="stylesheet">
<style>
  :root {
    --brand-blue: #1f8ae0;
    --brand-blue-deep: #1a7dd0;
    --ink-dark: #262626;
    --ink-text: #1c1c1c;
    --paper: #ffffff;
    --canvas-bg: #ffffff;
    --photo-light: #e9e9e6;
    --photo-mid: #b9b7b2;
    --photo-desk: #5a3a2c;
  }
  html, body {
    margin: 0;
    padding: 0;
    overflow: hidden;
    background: var(--canvas-bg);
  }
  .canvas {
    position: relative;
    width: 1200px;
    height: 1200px;
    overflow: hidden;
    background: var(--canvas-bg);
    font-family: "Roboto Condensed", "Arial Narrow", sans-serif;
  }
  .spread {
    position: absolute;
    left: 54px;
    top: 0;
    width: 1092px;
    height: 1200px;
  }

  /* Back panel — printed upside down so it reads correctly when folded */
  .back-panel {
    position: absolute;
    left: 0; top: 0;
    width: 1092px;
    height: 600px;
    background: linear-gradient(160deg, var(--brand-blue) 0%, var(--brand-blue-deep) 100%);
  }
  .back-content {
    position: absolute;
    left: 50%;
    top: 288px;
    transform: translate(-50%, -50%) rotate(180deg);
    text-align: center;
    color: var(--paper);
    width: 400px;
  }
  .back-brand {
    font-weight: 700;
    font-size: 44px;
    line-height: 1;
    margin: 0 0 18px;
    color: var(--paper);
  }
  .contact-name {
    font-weight: 700;
    font-size: 17px;
    color: var(--ink-text);
    margin: 0 0 4px;
  }
  .contact-line {
    font-size: 17px;
    line-height: 27px;
    margin: 0;
  }

  /* Front cover */
  .cover-photo {
    position: absolute;
    left: 0; top: 600px;
    width: 1092px;
    height: 384px;
    background:
      linear-gradient(115deg, #2e2e30 0%, #3b3b3d 14%, transparent 14.5%),
      radial-gradient(ellipse at 60% 70%, var(--photo-light) 0%, #d8d6d1 35%, transparent 60%),
      linear-gradient(180deg, var(--photo-mid) 0%, var(--photo-desk) 40%, #6b4a38 100%);
  }
  .cover-band {
    position: absolute;
    left: 0; top: 984px;
    width: 1092px;
    height: 216px;
  }
  .cover-band svg {
    position: absolute;
    inset: 0;
  }
  .cover-brand {
    position: absolute;
    left: 60px;
    top: 70px;
    font-weight: 700;
    font-size: 60px;
    line-height: 1;
    color: var(--brand-blue);
    margin: 0;
  }
  .cover-copy {
    position: absolute;
    right: 42px;
    top: 14px;
    text-align: right;
    margin: 0;
  }
  .cover-headline {
    font-weight: 700;
    font-size: 44px;
    color: var(--brand-blue);
    margin: 0;
    line-height: 1.1;
  }
  .cover-sub {
    font-weight: 700;
    font-size: 42px;
    color: var(--paper);
    margin: 6px 0 10px;
    line-height: 1.1;
  }
  .cover-offer {
    font-size: 28px;
    color: var(--paper);
    margin: 0;
    line-height: 1.25;
    text-transform: uppercase;
  }
</style>
</head>
<body>
<div class="canvas">
  <div class="spread">

    <section class="back-panel">
      <div class="back-content">
        <p class="back-brand">Clinic Harbor</p>
        <p class="contact-name">Clinic Harbor</p>
        <p class="contact-line">PO BOX 410522</p>
        <p class="contact-line">LAKE VISTA FL 30155</p>
        <p class="contact-line">555.318.4420</p>
        <p class="contact-line">555.902.6173</p>
        <p class="contact-line">info@clinicharbor.example</p>
      </div>
    </section>

    <div class="cover-photo" role="img" aria-label="Photo of colleagues at a desk reviewing printed charts beside a laptop, one holding a pen"></div>

    <section class="cover-band">
      <svg width="1092" height="216" viewBox="0 0 1092 216" aria-hidden="true">
        <rect x="0" y="0" width="1092" height="216" fill="var(--ink-dark)"/>
        <polygon points="0,35 472,35 568,216 0,216" fill="var(--paper)"/>
      </svg>
      <p class="cover-brand">Clinic Harbor</p>
      <div class="cover-copy">
        <p class="cover-headline">Cost Effective Resources</p>
        <p class="cover-sub">For Your</p>
        <p class="cover-offer">Cash Back Medical Plans</p>
        <p class="cover-offer">15% Wellness Medical Discount</p>
      </div>
    </section>

  </div>
</div>
</body>
</html>
```